Domestic Violence Consulting Firm needs double sided page flyer

We need a flyer for an upcoming Juvenile Justice conference in Florida that addresses a form of domestic violence called child to parent violence or parent abuse. This is when an adolescent is aggressive, abusive and violent toward a parent or caregiver and is arrested for Domestic Violence. The child attends Mending Roots Family Program with their parent who is the victim. We would like to see traditional DV photos but a with a new twist of the parent being the victim. The final design should promote shock to this new subject of domestic violence and interest to our program that addresses this subject. You can get more information about this at www.hearthwardsupport.example
Updates

REVISED CONTENT WITH A CALL TO ACTION Who we are: The silent suffering of parents abused by their adolescent is a serious and often hidden issue within families. Adolescent to Parent Abuse, internationally known as Child to Parent Violence is a complex family and public health problem. Stories from parents who are willing to speak about their abuse reveal the pain of victims who must by law care for their abuser. Abuse by teens in the home feels extremely violating as a youth steps out of their place in the natural family hierarchy. Understandably so, parents are often exhausted, carry deep grief as victims, feel shock and become isolated in shame and blame with nowhere to turn for understanding or help. Parents are not alone in their frustration and confusion associated with how to address Child to Parent Violence. Juvenile Justice Judges, State District Attorneys, Probation Officers, Child Welfare Case Managers and Law Enforcement Officers are often frustrated by who to turn to for professional services to intervene in this silent epidemic. Therefore, Mending Roots Consulting offers an array of consultative, collaborative and experienced professional services to a variety of clientele affected by Child to Parent Violence. Our specialized approach takes into account the serious ongoing need for safety of each family member. We have extensive experience with the nuances of this particular family and community challenge and offer a haven of safety to address this highly stigmatized topic. What we do: Mending Roots Family Program (bold) is conducted in a unique group setting within the juvenile justice probation and diversion program where families significantly reduce abuse and violence within the home. Parents and youth work together with trained facilitators through ten highly relational, psycho-educational sessions. Youth face their behaviors with weekly accountability and without minimizing, justifying or denying their disrespectful and abusive acts. Mending Roots Family Coaching (bold) is a private option for parents that encourages exploration of each family's values and individuality and facilitates discovery of their own personalized parenting style that respects the uniqueness of each family member and acknowledges the special history of each family unit. Mending Roots Training (bold) offers customized live and e-learning seminars, presentations, webinars and continued educational trainings for organizations. We are nationally recognized trainers in Adult and Youth Emotional Steady Aid and Balanced Living Renewal Map (BLRM). Train the trainer course for the Mending Roots Family Program is available upon request. Why we are the experts: We recognize that the relationship between a parent-child has a distinctiveness unlike those of intimate partners and requires a different approach. We address the societal concerns and needs of public safety, by providing youth with necessary and supportive accountability for their abuse behaviors through our Mending Roots Family Program. We honor each family’s culture, acknowledges the trauma of parenting a teen with abusive behaviors, nurtures each family’s strengths, and empowers all families to identify their individual needs. We motivate individuals, families and community with a focus on the global and basic human need for safety. We, the program designers, are recognized as subject matter experts on the topic and present at numerous local, state and national venues. We offer private consultative, collaborative and experienced professional services to agencies, communities and parents. Contact us today: facebook, website, twitter, linkedin (Call to action)

REVISED CONTENT FOR DOUBLE SIDED FLYER The silent suffering of parents abused by their adolescent is a serious and often hidden issue within families. Adolescent to Parent Abuse, internationally known as Child to Parent Violence is a complex family and public health problem. Stories from parents who are willing to speak about their abuse reveal the pain of victims who must by law care for their abuser. Abuse by teens in the home feels extremely violating as a youth steps out of their place in the natural family hierarchy and behaves with a squad of disrespectful and intense behaviors. Understandably so, parents are often exhausted, carry deep grief as victims, feel shock at experiencing their child’s abuse, and become isolated in shame and blame with nowhere to turn for understanding or help. Parents are not alone in their frustration and confusion associated with how to address Child to Parent Violence. Juvenile Justice Judges, State District Attorneys, Probation Officers, Child Welfare Case Managers and Law Enforcement Officers are often frustrated by who to turn to for professional services to intervene in this silent epidemic. Therefore, Mending Roots Consulting (bold) offers an array of consultative, collaborative and experienced professional services to a variety of clientele affected by Child to Parent Violence. Our specialized approach takes into account the serious ongoing need for safety of each family member. We have extensive experience with the nuances of this particular family and community challenge and offer a haven of safety to address this highly stigmatized topic. What we offer: Mending Roots Family Program (bold) is conducted in a unique group setting within the juvenile justice probation and diversion program where families significantly reduce abuse and violence within the home. Parents and youth work together with trained facilitators through ten highly relational, psycho-educational sessions. Youth face their behaviors with weekly accountability and without minimizing, justifying or denying their disrespectful and abusive acts. Mending Roots Family Coaching (bold) is a private option for parents that encourages exploration of each family's values and individuality and facilitates discovery of their own personalized parenting style that respects the uniqueness of each family member and acknowledges the special history of each family unit. Mending Roots Training (bold) offers customized live and e-learning seminars, webinars and continued educational trainings for organizations. We are nationally recognized trainers in Adult and Youth Emotional Steady Aid and Balanced Living Renewal Map (BLRM). Train the trainer course for the Mending Roots Family Program is available. How we are different: We recognize that the relationship between a parent-child has a distinctiveness unlike those of intimate partners that require a different approach. We address the societal concerns and needs of public safety, by providing youth with necessary and supportive accountability for their abuse behaviors. We honor each family’s culture, acknowledges the trauma of parenting a teen with abusive behaviors, nurturing each family’s strengths, and empower all families to identify their individual needs. We motivate individuals, families and communities with a focus on the global and basic human need for safety. We, the program designers, are recognized as subject matter experts on the topic and have presented at numerous local, state and national venues. We offer private consultative, collaborative and experienced professional services to agencies, communities and parents. Lets talk, contact us today to help your community address Child to Parent Violence (facebook, linkedin, website and twitter)

Target Market(s)

Department of Juvenile Justice, Law Enforcement, State Attorney, Probation Officers, Child Welfare Agency, Department of Child and Family, Legislators and Parents

Industry/Entity Type

Consulting

Font styles to use
Serif

Requirements
Must have
• Colorful, professional and double sided flyer with imagery similar to domestic violence but with an adolescent as the batterer towards the parent/caregiver. Description of how Mending Roots Consulting provides a evidenced promised 10 week community based program designed to reduce teen abuse and violence within the home. And consulting services such as train the trainer for the program, presentations, parent coaching and independent educational consulting services to parents.
Nice to have
• OCR for the website

```html
<!DOCTYPE html>
<html lang="en">
<head>
<meta charset="utf-8">
<title>Mending Roots Consulting – Double Sided Flyer</title>
<link rel="stylesheet" href="https://fonts.googleapis.com/css2?family=Arimo:ital,wght@0,400;0,700;1,400&display=swap">
<style>
  :root {
    --royal: #2f4fe0;
    --royal-deep: #1f35b8;
    --sky-line: #c9d3f5;
    --hope-red: #e0261c;
    --ink: #1c1c1c;
    --label-bg: #1a1a1a;
    --link-blue: #2f6fd6;
    --paper: #ffffff;
    --backdrop: #e4e6ea;
    --logo-tone: #e8771f;
  }
  * { box-sizing: border-box; margin: 0; padding: 0; }
  html, body { width: 1200px; height: 1200px; overflow: hidden; }
  body {
    background: var(--backdrop);
    font-family: "Arimo", Arial, sans-serif;
    color: var(--ink);
    position: relative;
  }
  .sheet {
    position: absolute;
    top: 241px;
    width: 555px;
    height: 718px;
    background: var(--paper);
    overflow: hidden;
    box-shadow: 0 2px 10px rgba(0,0,0,.18);
  }
  .sheet--front { left: 30px; }
  .sheet--back { left: 615px; }

  /* header band */
  .masthead { position: relative; height: 118px; }
  .masthead svg { position: absolute; inset: 0; }
  .brand {
    position: absolute; left: 20px; top: 14px;
    display: flex; align-items: flex-start; gap: 12px;
  }
  .brand__mark {
    width: 62px; height: 62px; border-radius: 50%;
    background: var(--logo-tone); flex: none;
  }
  .brand__name {
    color: #fff; font-weight: 700; font-size: 23px; line-height: 1.05;
  }
  .brand__tagline {
    color: #fff; font-weight: 700; font-size: 15px; line-height: 1.15; margin-top: 3px;
  }
  .brand__tagline .hope { color: var(--hope-red); }
  .brand__tagline .indent { display: block; padding-left: 40px; }

  .content { padding: 0 26px; font-size: 9.2px; line-height: 1.32; }
  .content p { margin-bottom: 7px; text-align: justify; }
  .program-label {
    background: var(--label-bg); color: #fff; padding: 1px 3px; font-weight: 700;
  }
  .link-text { color: var(--link-blue); }

  .photo { display: block; }
  .photo--portrait {
    float: right; width: 92px; height: 100px; margin: 0 0 6px 10px;
    background: linear-gradient(160deg, #3a67c9, #c7a17f 60%, #e5c3a8);
  }
  .photo--children {
    float: right; width: 150px; height: 100px; margin: 4px 0 6px 10px;
    background: linear-gradient(135deg, #8fc6e6, #d9a57c 55%, #f2d2b6);
  }
  .photo-row {
    position: absolute; left: 0; right: 0; bottom: 22px;
    display: flex; gap: 6px; height: 128px; padding: 0 0 0 0;
  }
  .photo-row .photo { flex: 1; }
  .photo--toddler { background: linear-gradient(150deg, #4a6b8a, #d7b49a); }
  .photo--beach { background: linear-gradient(180deg, #9fd0ef 0%, #cfe6f3 55%, #e6d5b0 100%); }
  .photo--mother { background: linear-gradient(140deg, #c08a66, #f0d0b4 60%, #6b4a3a); }
  .footer-bar {
    position: absolute; left: 0; right: 0; bottom: 0; height: 16px; background: var(--royal);
  }

  /* back side */
  .topband { position: relative; height: 78px; }
  .topband svg { position: absolute; inset: 0; }
  .content--back { padding-top: 6px; }
  .question {
    color: var(--royal); font-size: 15.5px; line-height: 1.2; text-align: center;
    margin: 4px 0 10px;
  }
  .back-photos {
    display: flex; gap: 8px; padding: 0 26px; height: 170px; margin-top: 6px;
  }
  .photo--family-walk { flex: 1; background: linear-gradient(180deg, #dfe9f1 0%, #f4f6f7 60%, #d8cbb4 100%); }
  .photo--family-beach { flex: 1; background: linear-gradient(180deg, #7fb8e4 0%, #b9d9ee 45%, #d9b79a 100%); }
  .contact-band { position: absolute; left: 0; right: 0; bottom: 0; height: 150px; }
  .contact-band svg { position: absolute; inset: 0; }
  .contact-list {
    position: absolute; right: 40px; bottom: 22px;
    color: #fff; font-size: 15px; line-height: 1.35; text-align: center; list-style: none;
  }
</style>
</head>
<body>

<section class="sheet sheet--front">
  <header class="masthead">
    <svg width="555" height="118" viewBox="0 0 555 118" aria-hidden="true">
      <path d="M0 0 H555 V82 Q300 120 0 104 Z" fill="var(--royal)"/>
      <path d="M0 104 Q300 120 555 82" fill="none" stroke="var(--sky-line)" stroke-width="4"/>
    </svg>
    <div class="brand">
      <div class="brand__mark"></div>
      <div>
        <div class="brand__name">Mending Roots Consulting, Inc.</div>
        <div class="brand__tagline"><span class="hope">HOPE</span> for families experiencing teen
          <span class="indent">abuse and violence withing the home.</span></div>
      </div>
    </div>
  </header>

  <div class="content">
    <div class="photo photo--portrait" role="img" aria-label="Portrait photo of the program director"></div>
    <p>The silent topic of teen abuse and violence toward a parent or guardian is an all too common family secret requiring an understanding that is different from traditional domestic violence theories. Utilizing a replicable, innovative collaboration model that incorporates the <span class="link-text">Community Wellness Services Agency (CWSA) System of Care (SOC)</span> guiding principles and values, <span class="link-text">Mending Roots Family Program (MRFP)</span> currently implements psycho-educational groups within the juvenile justice probation and diversion program where families significantly reduce abuse and violence within the home. MRFP is an emerging curriculum including attention to progression from research, to pilot, to scale.</p>
    <p>Stories from parents who are willing to speak about their abuse reveal the pain of victims who must by law care for their abuser. The escalation of a youth's feelings and behaviors into a pattern of abusive behaviors is often met with disbelief on the part of the victim and family unit. Uncertainty exists among the parents on what is 'normal' for teens in today's culture, and they often wonder if the abuse is a passing phase like so many other phases of child and human development. Abuse by teens in the home feels extremely violating as a youth steps out of their place in the natural family hierarchy and behaves with a cadre of disrespectful and intense behaviors. Understandably so, parents are often exhausted, carry deep grief as victims, feel shock at experiencing their child's abusive lashing out, and become isolated in shame and blame with nowhere to turn for understanding or help.</p>
    <div class="photo photo--children" role="img" aria-label="Photo of smiling children lying together"></div>
    <p><span class="program-label">Mending Roots Family Program</span> is conducted in a unique group setting. Through ten highly relational, psycho-educational sessions, parents and youth work together with other families. Families are greatly encouraged when they discover they are not alone in the journey of abuse. MRFP honors each family's culture, acknowledges the trauma of parenting a teen with abusive behaviors, nurtures each family's strengths, and empowers all families to identify their individual needs. MRFP provides a supportive and safe place for families to explore and make changes pertinent to their situation.</p>
    <p><span class="program-label">Mending Roots Family Program</span> provides both parents and youth the time to grow together in their understanding of abuse. Together they acquire a variety of skills and concepts that strengthen them in this challenging area of life. MRFP acknowledges parents as experts in their own families. Youth face their behaviors with accountability and without minimizing, justifying or denying their disrespectful and abusive actions. Participants forge the bonds of familial respect and reduce the struggles of disrespect, abuse and violence. Together, parents and youth create shared goals for mutual respect and decreasing abuse.</p>
  </div>

  <div class="photo-row">
    <div class="photo photo--toddler" role="img" aria-label="Photo of a parent holding a young child"></div>
    <div class="photo photo--beach" role="img" aria-label="Photo of a family walking hand in hand on a beach"></div>
    <div class="photo photo--mother" role="img" aria-label="Photo of a mother smiling with her baby"></div>
  </div>
  <div class="footer-bar"></div>
</section>

<section class="sheet sheet--back">
  <header class="topband">
    <svg width="555" height="78" viewBox="0 0 555 78" aria-hidden="true">
      <path d="M0 0 H555 V70 Q280 30 0 52 Z" fill="var(--royal)"/>
      <path d="M0 52 Q280 30 555 70" fill="none" stroke="var(--sky-line)" stroke-width="4"/>
    </svg>
  </header>

  <div class="content content--back">
    <p><span class="program-label">Mending Roots Family Program</span> groups offer a respite of civility, personal growth, and encouragement during the storms of family life. MRFP addresses the societal concerns and needs of public safety, provides youth with necessary and supportive accountability for their abuse, and builds competency in developmentally appropriate social and emotional skills needed by teens to replace their abusive and violent behaviors. It is true; hope and healing are possible for families that have been ravaged and devastated by teen abuse and violence.</p>
    <h2 class="question">What makes Mending Roots Family Program so effective<br>at reducing teen abuse and violence in the home?</h2>
    <p>We understand that traditional domestic violence battery inventions, concepts, and philosophies for adult intimate partner abuse is not developmentally appropriate for adolescents and traditional approaches result in an increase of teen abuse and violence within the home.</p>
    <p>We recognize that the relationship between a parent-child has a distinctiveness unlike those of intimate partners.</p>
    <p>We motivate attendees with a focus on the global and basic human need for safety.</p>
    <p>We provide a relationship based positive peer setting where teens are weekly accountable in a group setting for their behaviors toward parents.</p>
    <p>We emphasize on safety combined with the parent component serves as a highly protective factor for the contagion challenge typical in delinquent settings.</p>
    <p>We facilitate a safe, open, and non-judgmental environment where family units of any culture can work together as a parent child team to address the abusive behaviors that are particular to their home.</p>
    <p>We deliver lessons that target key concepts and universally recognized communication skills to address behaviors and the underlying emotions that developed into domestic violence charge.</p>
    <p>We incorporate the Community Wellness Services Agency (CWSA) System of Care Principles and Values.</p>
    <p>We, the program designers, are recognized as subject matter experts on the topic and have presented at numerous state and national venues.</p>
    <p>We understand the complex nuances of this form of domestic violence having served over 150 teens charged with Domestic Violence or Battery against a caregiver with a total of over 200 individuals including parents or other caregivers.</p>
  </div>

  <div class="back-photos">
    <div class="photo photo--family-walk" role="img" aria-label="Photo of a family holding hands in a row on a bright field"></div>
    <div class="photo photo--family-beach" role="img" aria-label="Photo of a father and mother holding two young children at the beach"></div>
  </div>

  <footer class="contact-band">
    <svg width="555" height="150" viewBox="0 0 555 150" aria-hidden="true">
      <path d="M0 40 Q260 10 555 70 V150 H0 Z" fill="var(--royal)"/>
      <path d="M0 40 Q260 10 555 70" fill="none" stroke="var(--sky-line)" stroke-width="4"/>
    </svg>
    <ul class="contact-list">
      <li>www.hearthwardsupport.example</li>
      <li>https://social.example/MRconsulting</li>
      <li>https://microposts.example/parent_care</li>
    </ul>
  </footer>
</section>

</body>
</html>
```